Creative Web Design - Intl Market Research Company

We need an innovative web design for an emerging company into the international market research marketplace.

The company, Halvenor Associates, is a Trade, Investment, and Market Research company. Halvenor offers domestic and international companies increased success in the U.S. marketplace by providing a variety of services. (seen on attached brochure)

The website should be cutting edge and creative while having an easy navigation. The color is not fixed and attached logo is not finalized, feel free to post anything from conservative to progressive options. Keep in mind target customers are domestic and international businesses looking to emerge/improve in the U.S. marketplace.

Additional Company information is located in the attached documentation. The documentation is outdated & winner will have priority standing for our next projects.(logo & document re-design)

I have received a few e-mail requests and have updated the status to guaranteed payment.

Thanks!

Target Market(s)

Any company, foreign and domestic, looking to introduce their product into the U.S. marketplace.

Industry/Entity Type

Market Research

Requirements
Must have
• Easy Navigation
Should not have
• Too many buttons
Difficult navigation
Excessive Typography

```html
<!DOCTYPE html>
<html lang="en">
<head>
<meta charset="utf-8">
<title>Halvenor Associates</title>
<link href="https://fonts.googleapis.com/css2?family=Open+Sans:wght@400;600;700&family=Roboto:wght@400;500;700&family=Roboto+Condensed:wght@700&display=swap" rel="stylesheet">
<style>
:root{
  --blue:#1f64a6;
  --blue-dark:#174f86;
  --blue-light:#1aa3d6;
  --gold:#e8b84a;
  --gold-text:#d89a12;
  --ink:#2e2e2e;
  --body:#3c3c3c;
  --page:#f1f1f1;
  --card:#fafafa;
  --line:#d6d6d6;
  --footer:#3b3b3b;
  --footer-line:#4c4c4c;
  --footer-text:#e6e6e6;
}
*{box-sizing:border-box;margin:0;padding:0}
html,body{width:1093px;height:1200px;overflow:hidden}
body{background:var(--page);font-family:"Roboto",Arial,sans-serif;color:var(--body)}
.canvas{position:relative;width:1093px;height:1200px;overflow:hidden;background:linear-gradient(#f7f7f7,#ececec)}
.abs{position:absolute}
a{color:inherit;text-decoration:none}

/* header */
.header{left:0;top:0;width:1093px;height:94px;background:linear-gradient(#fff,#efefef)}
.brand{left:128px;top:14px;display:flex;align-items:center;gap:14px}
.brand-mark{width:66px;height:66px;border-radius:50%;background:var(--gold)}
.brand-name{font-family:"Open Sans",sans-serif;font-weight:700;font-size:25px;color:var(--blue);line-height:1}
.brand-tag{font-family:"Open Sans",sans-serif;font-weight:600;font-size:11px;color:#333;margin-top:6px}
.contact-top{left:808px;top:26px;font-family:"Open Sans",sans-serif;color:var(--blue)}
.contact-top div{display:flex;align-items:center;gap:8px}
.phone{font-size:17px;font-weight:700}
.email{font-size:11px;font-weight:600;margin-top:8px}
.ico-sq{width:16px;height:16px;border-radius:3px;background:var(--gold);display:flex;align-items:center;justify-content:center}

/* nav */
.nav{left:0;top:94px;width:1093px;height:32px;background:linear-gradient(var(--blue),var(--blue-dark))}
.nav-item{position:absolute;top:0;height:32px;line-height:32px;font-family:"Open Sans",sans-serif;font-weight:700;font-size:10.5px;color:#fff;text-align:center}
.nav-item.active{background:var(--gold);color:#333}
.nav-sep{position:absolute;top:0;width:1px;height:32px;background:#3a7fc0}
.search{left:796px;top:103px;width:169px;height:18px;border-radius:9px;background:#fff;font-size:10px;color:#999;padding-left:13px;line-height:18px}
.search-btn{position:absolute;right:2px;top:2px;width:14px;height:14px;border-radius:50%;background:var(--blue)}

/* hero */
.hero{left:128px;top:135px;width:837px;height:282px;border-radius:4px;overflow:hidden;background:radial-gradient(ellipse at 55% 50%,var(--blue-light),#0d6fa8 70%,#0b5688)}
.hero-photo{position:absolute;right:0;top:20px;width:440px;height:262px;background:linear-gradient(180deg,rgba(255,255,255,.08),rgba(20,40,60,.35))}
.hero-title{left:24px;top:68px;font-family:"Roboto Condensed",sans-serif;font-weight:700;font-size:37px;line-height:1;color:#fff}
.hero-text{left:22px;top:112px;width:400px;font-family:"Open Sans",sans-serif;font-size:17.5px;line-height:26px;color:#fff}
.dots{left:28px;top:258px;display:flex;gap:10px}
.dots span{width:9px;height:9px;border-radius:50%;background:#cfd6dc}
.dots span.on{background:var(--blue)}

/* feature boxes */
.box{top:442px;width:187px;height:230px;background:var(--card);border:1px solid var(--line);border-radius:6px;overflow:hidden}
.box-head{height:50px;background:linear-gradient(#2a78bd,var(--blue-dark));border-bottom:3px solid var(--gold);display:flex;align-items:center;padding-left:9px;gap:14px}
.box-icon{width:40px;height:40px;border-radius:50%;background:#f2f2f2;display:flex;align-items:center;justify-content:center;flex:none}
.box-title{font-family:"Open Sans",sans-serif;font-weight:700;font-size:13.5px;line-height:18px;color:#fff;text-align:center;width:110px}
.box-body{padding:12px 11px 0 11px;font-size:10.8px;line-height:15.6px;color:#333}
.ticks{list-style:none;padding:7px 8px 0 8px;font-size:10.8px;color:#333}
.ticks li{display:flex;gap:9px;line-height:14.5px;margin-bottom:3.4px}
.ticks.wide li{margin-bottom:7.5px}
.ticks svg{flex:none;margin-top:2px}
.read{position:absolute;right:9px;bottom:9px;font-family:"Open Sans",sans-serif;font-weight:700;font-size:11.5px;color:var(--blue)}

/* welcome */
.h2{font-family:"Open Sans",sans-serif;font-weight:600;font-size:19px;color:#222}
.h2 em{font-style:normal;color:var(--blue)}
.dash{border-top:1px dashed #cfcfcf}
.lead{left:130px;top:752px;width:612px;font-weight:700;font-size:11.2px;line-height:18px;color:#222;letter-spacing:.25px}
.copy{left:128px;top:796px;width:614px;font-size:10.8px;line-height:19px;color:#444}
.btn{height:20px;line-height:20px;border-radius:4px;background:#3c3c3c;color:#fff;font-size:10.5px;font-weight:500;text-align:center;width:72px}
.sources{left:779px;top:752px;list-style:none}
.sources li{display:flex;gap:12px;align-items:center;height:29px;font-size:11.5px;color:#333}

/* news */
.news{left:128px;top:937px;width:837px;height:39px;background:linear-gradient(#fff,#ededed);box-shadow:0 2px 2px rgba(0,0,0,.2)}
.news-tag{position:absolute;left:0;top:0;width:102px;height:39px;background:var(--blue);clip-path:polygon(0 0,80% 0,100% 50%,80% 100%,0 100%);font-family:"Open Sans",sans-serif;font-weight:700;font-size:14.5px;line-height:16px;color:#fff;padding:3px 0 0 23px}
.news-date{position:absolute;left:113px;top:12px;font-size:11px;font-weight:500;color:var(--gold-text)}
.news-text{position:absolute;left:209px;top:11px;font-size:11.5px;font-style:italic;font-weight:500;color:#222}

/* footer */
.footer{left:0;top:1012px;width:1093px;height:188px;background:var(--footer);color:var(--footer-text)}
.f-sep{position:absolute;top:0;width:1px;height:188px;background:var(--footer-line)}
.f-head{position:absolute;top:20px;font-family:"Open Sans",sans-serif;font-weight:600;font-size:12.5px;color:#fff;padding-bottom:11px;border-bottom:1px dashed #777}
.f-list{position:absolute;list-style:none;font-size:10.5px}
.f-list li{height:18.5px;display:flex;gap:8px;align-items:center}
.f-contact{position:absolute;left:316px;top:59px;font-size:10.3px;line-height:17px}
.f-row{display:flex;gap:12px}
.f-row .ic{width:12px;flex:none}
.f-social{position:absolute;left:509px;top:60px;font-size:9.8px;font-weight:700;color:#fff}
.f-social div{display:flex;align-items:center;gap:12px;height:28px}
.f-social .sq{width:17px;height:17px;border-radius:3px;background:#f2f2f2}
.f-input{position:absolute;left:711px;top:59px;width:166px;height:24px;background:#fff;border-radius:2px;font-size:11px;font-style:italic;color:#555;padding:5px 7px}
.f-sub{position:absolute;left:890px;top:61px;width:64px;height:20px;line-height:20px;text-align:center;background:#555;border:1px solid #777;border-radius:2px;font-size:10.5px;color:#fff}
.cards{position:absolute;left:713px;top:102px;display:flex;gap:17px}
.cards span{width:42px;height:26px;border-radius:3px;background:#f5f5f5;font-size:8px;font-weight:700;color:var(--blue);display:flex;align-items:center;justify-content:center}
.copyright{position:absolute;left:713px;top:153px;font-size:9px;color:#ddd}
</style>
</head>
<body>
<div class="canvas">

  <header class="abs header">
    <div class="abs brand">
      <span class="brand-mark"></span>
      <div>
        <div class="brand-name">Halvenor Associates</div>
        <div class="brand-tag">Investment, and Market Research company</div>
      </div>
    </div>
    <div class="abs contact-top">
      <div class="phone"><span class="ico-sq"><svg width="10" height="10" viewBox="0 0 10 10"><path d="M2 1l2 2-1 1c1 2 2 3 3 3l1-1 2 2-1.5 1.5C4 9 1 6 .5 2.5z" fill="#fff"/></svg></span>1.555.204.7730</div>
      <div class="email"><span class="ico-sq"><svg width="10" height="8" viewBox="0 0 10 8"><rect x=".5" y=".5" width="9" height="7" fill="none" stroke="#fff"/><path d="M.5 .5l4.5 4 4.5-4" fill="none" stroke="#fff"/></svg></span>info@halvenor-mail.net</div>
    </div>
  </header>

  <nav class="abs nav">
    <a class="nav-item active" style="left:128px;width:78px">HOME</a>
    <a class="nav-item" style="left:222px;width:80px">ABOUT US</a>
    <span class="nav-sep" style="left:319px"></span>
    <a class="nav-item" style="left:332px;width:80px">SERVICES</a>
    <span class="nav-sep" style="left:426px"></span>
    <a class="nav-item" style="left:439px;width:100px">CATEGORIES</a>
    <span class="nav-sep" style="left:553px"></span>
    <a class="nav-item" style="left:566px;width:100px">OUR SOURCES</a>
    <span class="nav-sep" style="left:681px"></span>
    <a class="nav-item" style="left:695px;width:100px">CONTACT US</a>
  </nav>
  <div class="abs search">Search Reports<span class="search-btn"></span></div>

  <section class="abs hero">
    <div class="hero-photo" role="img" aria-label="Photo of a diverse group of business professionals standing with arms crossed in front of a faint world map"></div>
    <h1 class="abs hero-title">Halvenor Associates</h1>
    <p class="abs hero-text">We prepare overall plan for Registrar selection and registration to US or foreign national ISO 9000 schemes and provide ISO staff training.</p>
    <div class="abs dots"><span class="on"></span><span></span><span></span><span></span></div>
  </section>

  <article class="abs box" style="left:129px">
    <div class="box-head">
      <span class="box-icon"><svg width="20" height="20" viewBox="0 0 20 20"><circle cx="10" cy="10" r="8" fill="none" stroke="#555" stroke-width="1.5"/><path d="M2 10h16M10 2c-4 4-4 12 0 16M10 2c4 4 4 12 0 16" fill="none" stroke="#555"/></svg></span>
      <h3 class="box-title">GLOBAL DATA COLLECTION</h3>
    </div>
    <p class="box-body">The world is fast becoming a global economy and businesses wanting to succeed in this highly competitive environment must have access to up-to-date business information. We provide current, relevant information to enhance your chances of success.</p>
    <a class="read">Read More »</a>
  </article>

  <article class="abs box" style="left:342px">
    <div class="box-head">
      <span class="box-icon"><svg width="18" height="20" viewBox="0 0 18 20"><rect x="1" y="1" width="14" height="18" fill="none" stroke="#555" stroke-width="1.5"/><path d="M4 6h8M4 10h8M4 14h5" stroke="#555"/></svg></span>
      <h3 class="box-title">MARKET RESEARCH</h3>
    </div>
    <p class="box-body">If you are a bit stuck with your provider having reached 'productivity stagnation,' allow us to breathe life into your process outsourcing engagements. We have a highly scalable blended client services and delivery model that continually pushes the limits of operational excellence.</p>
    <a class="read">Read More »</a>
  </article>

  <article class="abs box" style="left:561px">
    <div class="box-head">
      <span class="box-icon"><svg width="22" height="22" viewBox="0 0 22 22"><circle cx="11" cy="11" r="7" fill="none" stroke="#777" stroke-width="4" stroke-dasharray="3 2.5"/><circle cx="11" cy="11" r="3" fill="#777"/></svg></span>
      <h3 class="box-title">OUR<br>SERVICE</h3>
    </div>
    <ul class="ticks">
      <li><svg width="12" height="10"><path d="M1 5l3 4 7-8" fill="none" stroke="#e8a020" stroke-width="1.5"/></svg>Importers</li>
      <li><svg width="12" height="10"><path d="M1 5l3 4 7-8" fill="none" stroke="#e8a020" stroke-width="1.5"/></svg>Agents/Representatives</li>
      <li><svg width="12" height="10"><path d="M1 5l3 4 7-8" fill="none" stroke="#e8a020" stroke-width="1.5"/></svg>Distributors</li>
      <li><svg width="12" height="10"><path d="M1 5l3 4 7-8" fill="none" stroke="#e8a020" stroke-width="1.5"/></svg>Manufacturers</li>
      <li><svg width="12" height="10"><path d="M1 5l3 4 7-8" fill="none" stroke="#e8a020" stroke-width="1.5"/></svg>Joint Venture Partners</li>
      <li><svg width="12" height="10"><path d="M1 5l3 4 7-8" fill="none" stroke="#e8a020" stroke-width="1.5"/></svg>Manufacturing Under License Partners</li>
      <li><svg width="12" height="10"><path d="M1 5l3 4 7-8" fill="none" stroke="#e8a020" stroke-width="1.5"/></svg>Investment Partners</li>
    </ul>
    <a class="read">Read More »</a>
  </article>

  <article class="abs box" style="left:777px">
    <div class="box-head">
      <span class="box-icon"><svg width="20" height="20" viewBox="0 0 20 20"><circle cx="8" cy="8" r="5.5" fill="none" stroke="#555" stroke-width="1.8"/><path d="M12 12l6 6" stroke="#555" stroke-width="2.5"/></svg></span>
      <h3 class="box-title">MARKET MATCHING</h3>
    </div>
    <ul class="ticks wide">
      <li><svg width="12" height="10"><path d="M1 5l3 4 7-8" fill="none" stroke="#e8a020" stroke-width="1.5"/></svg>Research Appropriate Firms</li>
      <li><svg width="12" height="10"><path d="M1 5l3 4 7-8" fill="none" stroke="#e8a020" stroke-width="1.5"/></svg>Present Your Product/Service</li>
      <li><svg width="12" height="10"><path d="M1 5l3 4 7-8" fill="none" stroke="#e8a020" stroke-width="1.5"/></svg>Select Potential Matches</li>
      <li><svg width="12" height="10"><path d="M1 5l3 4 7-8" fill="none" stroke="#e8a020" stroke-width="1.5"/></svg>Introduce You to Companies Specifically Interested in Your Product/Service</li>
    </ul>
    <a class="read">Read More »</a>
  </article>

  <h2 class="abs h2" style="left:130px;top:708px">Welcome to <em>Halvenor Associates</em></h2>
  <div class="abs dash" style="left:130px;top:739px;width:617px"></div>
  <p class="abs lead">Lorem ipsum dolor sit amet consectetur adipisicing elitsed do eiusmod tempor incididunt ut labore et dolore aliqua. Ut enim ad minim veniam.</p>
  <p class="abs copy">Lorem ipsum dolor sit amet consectetur adipisicing elitsed do eiusmod tempor incididunt ut labore et dolore aliqua. Ut enim ad minim veniam, quis nostrud exercitation ullamco laboris nisi ut aliquip ex ea commodo consequat. Duis aute irure dolor in reprehenderit in voluptate velit esse cillum dolore eu fugiat nul pariatur. Excepteur occaecat cupidatat non proident, sunt in culpa qui officia deserunt mollit anim id est laborum. Lorem ipsum dolor sit amet, consectetur adipisicing elit, sed do eiusmod tempor incididunt consectetur adipisicing elitsed do eiusmod tempor incididunt ut labore et dolore aliqua Ut enim.</p>
  <a class="abs btn" style="left:677px;top:899px">Read more</a>

  <h2 class="abs h2" style="left:783px;top:708px">Our <em>Sources</em></h2>
  <div class="abs dash" style="left:779px;top:739px;width:187px"></div>
  <ul class="abs sources">
    <li><svg width="6" height="10"><path d="M1 1l4 4-4 4" fill="none" stroke="#e8a020" stroke-width="1.4"/></svg>ON LINE DATABASES</li>
    <li><svg width="6" height="10"><path d="M1 1l4 4-4 4" fill="none" stroke="#e8a020" stroke-width="1.4"/></svg>CD ROM DATABASES</li>
    <li><svg width="6" height="10"><path d="M1 1l4 4-4 4" fill="none" stroke="#e8a020" stroke-width="1.4"/></svg>INDUSTRY ASSOCIATIONS</li>
    <li><svg width="6" height="10"><path d="M1 1l4 4-4 4" fill="none" stroke="#e8a020" stroke-width="1.4"/></svg>INDUSTRY EXPERTS</li>
    <li><svg width="6" height="10"><path d="M1 1l4 4-4 4" fill="none" stroke="#e8a020" stroke-width="1.4"/></svg>GOVERNMENT EXPERTS</li>
  </ul>
  <a class="abs btn" style="left:893px;top:899px">Read more</a>

  <div class="abs news">
    <div class="news-tag">Latest<br>News</div>
    <span class="news-date">March 6,2013 <span style="color:#555;margin-left:8px">|</span></span>
    <span class="news-text">Lorem ipsum dolor sit amet, consectetuer adipiscing elit, sed diam nonummy nibh euismod tincidunt ut laoreet .</span>
  </div>

  <footer class="abs footer">
    <span class="f-sep" style="left:290px"></span>
    <span class="f-sep" style="left:477px"></span>
    <span class="f-sep" style="left:648px"></span>

    <h4 class="f-head" style="left:138px;width:120px">Quick Links</h4>
    <ul class="f-list" style="left:138px;top:58px">
      <li><svg width="4" height="7"><path d="M.5.5l3 3-3 3" fill="none" stroke="#ddd"/></svg>Home</li>
      <li><svg width="4" height="7"><path d="M.5.5l3 3-3 3" fill="none" stroke="#ddd"/></svg>About Us</li>
      <li><svg width="4" height="7"><path d="M.5.5l3 3-3 3" fill="none" stroke="#ddd"/></svg>Services</li>
      <li><svg width="4" height="7"><path d="M.5.5l3 3-3 3" fill="none" stroke="#ddd"/></svg>Categories</li>
      <li><svg width="4" height="7"><path d="M.5.5l3 3-3 3" fill="none" stroke="#ddd"/></svg>Our Sources</li>
      <li><svg width="4" height="7"><path d="M.5.5l3 3-3 3" fill="none" stroke="#ddd"/></svg>Contact Us</li>
    </ul>

    <h4 class="f-head" style="left:316px;width:122px">Contact Us</h4>
    <div class="f-contact">
      <div class="f-row"><span class="ic"><svg width="10" height="13"><path d="M5 12C1 7 1 5 1 4.5a4 4 0 0 1 8 0C9 5 9 7 5 12z" fill="#ccc"/></svg></span><div><b style="color:#fff">48 Harbor Crest Road,</b><br>Suite B Linden Bay,<br>CA 90410</div></div>
      <div class="f-row" style="margin-top:3px"><span class="ic"><svg width="11" height="11" viewBox="0 0 10 10"><path d="M2 1l2 2-1 1c1 2 2 3 3 3l1-1 2 2-1.5 1.5C4 9 1 6 .5 2.5z" fill="#ccc"/></svg></span>Tel : 1.555.204.7730</div>
      <div class="f-row" style="margin-top:4px"><span class="ic"><svg width="12" height="11"><rect x="3" y="0" width="6" height="3" fill="#ccc"/><rect x="0" y="3" width="12" height="5" fill="#ccc"/><rect x="3" y="7" width="6" height="4" fill="#ddd"/></svg></span>Fax : 1.555.204.7731</div>
    </div>

    <h4 class="f-head" style="left:505px;width:122px">Follow Us</h4>
    <div class="f-social">
      <div><span class="sq"></span>Friendwall</div>
      <div><span class="sq"></span>Chirpline</div>
      <div><span class="sq"></span>Workweb</div>
    </div>

    <h4 class="f-head" style="left:711px;width:230px;top:17px">Newsletter</h4>
    <div class="f-input">Email Address</div>
    <div class="f-sub">Subscribe</div>
    <div class="cards"><span>Brimcard</span><span>Lunopay</span><span>Corvix</span><span>Tessaly</span></div>
    <p class="copyright">Copyright © 2013 Halvenor Associates .All Rights Reserved.</p>
  </footer>

</div>
</body>
</html>
```